Geschäftspapiere für Zimmerei
Zielgruppe
Zimmerei Holzbau
Aufgabenstellung
Das Logo
Gerold Wenck
Lindenweg 42
87634 Tannried
ein Wasserzeichen oder eine dezente Zeichnung mit einbringen währe schön

```html
<!DOCTYPE html>
<html lang="de">
<head>
<meta charset="utf-8">
<title>Briefpapier Zimmerei Wenck</title>
<link href="https://fonts.googleapis.com/css2?family=Montserrat:wght@400;600;700&display=swap" rel="stylesheet">
<style>
  :root {
    --backdrop: #b4b4b4;
    --paper: #f7f7f7;
    --green: #2a7a55;
    --red: #dc2e37;
    --text-grey: #6a6a6a;
    --mark-tone-a: #ebebeb;
    --mark-tone-b: #f3f3f3;
  }
  * { margin: 0; padding: 0; box-sizing: border-box; }
  html, body {
    width: 1200px; height: 900px; overflow: hidden;
    background: var(--backdrop);
    font-family: "Montserrat", sans-serif;
  }
  .letterhead {
    position: absolute; left: 310px; top: 40px;
    width: 580px; height: 820px;
    background: var(--paper);
    overflow: hidden;
  }
  .brand {
    position: absolute; right: 30px; top: 64px;
    display: flex; align-items: center; gap: 8px;
    font-weight: 700; font-size: 20px; line-height: 24px; color: var(--green);
    white-space: nowrap;
  }
  .brand-dot {
    width: 13px; height: 13px; border-radius: 50%;
    background: var(--red); flex: none;
  }
  .sender {
    position: absolute; left: 440px; top: 180px;
    font-style: normal;
    color: var(--green); font-size: 11px; line-height: 14px;
    white-space: nowrap;
  }
  .sender-company { font-weight: 700; }
  .sender-name { font-weight: 400; }
  .sender-name strong { font-weight: 700; }
  .sender-address {
    display: flex; gap: 7px; margin-top: 9px;
    color: var(--text-grey); font-size: 8.5px; line-height: 12.5px;
  }
  .pin-icon { width: 12px; height: 18px; margin-top: 2px; flex: none; }
  .watermark {
    position: absolute; left: 402px; top: 610px;
    width: 178px; height: 180px;
    background: radial-gradient(ellipse at 60% 45%, var(--mark-tone-a), var(--mark-tone-b) 55%, transparent 75%);
  }
  .footer-bands {
    position: absolute; left: 0; bottom: 0; width: 580px; height: 34px;
  }
</style>
</head>
<body>
  <main class="letterhead">
    <div class="brand"><span class="brand-dot"></span>Zimmerei Wenck</div>

    <address class="sender">
      <div class="sender-company">Zimmerei Holzbau</div>
      <div class="sender-name">Gerold <strong>Wenck</strong></div>
      <div class="sender-address">
        <svg class="pin-icon" viewBox="0 0 12 18" aria-hidden="true">
          <path d="M6 1.2a4.3 4.3 0 0 0-4.3 4.3C1.7 8.7 6 13 6 13s4.3-4.3 4.3-7.5A4.3 4.3 0 0 0 6 1.2z" fill="none" stroke="var(--green)" stroke-width="1.3"/>
          <circle cx="6" cy="5.5" r="1.4" fill="var(--green)"/>
          <line x1="2.5" y1="16.5" x2="9.5" y2="16.5" stroke="var(--green)" stroke-width="1.4"/>
        </svg>
        <span>Lindenweg 42<br>87634 Tannried</span>
      </div>
    </address>

    <div class="watermark" role="img" aria-label="Dezentes Wasserzeichen: Steinbock vor Berggipfeln"></div>

    <svg class="footer-bands" viewBox="0 0 580 34" preserveAspectRatio="none" aria-hidden="true">
      <path d="M290 22 C400 19 500 14 580 9 L580 19 C480 21 380 22 290 22 Z" fill="var(--green)"/>
      <path d="M0 9 C150 18 300 23 580 23 L580 34 L0 34 Z" fill="var(--red)"/>
    </svg>
  </main>
</body>
</html>
```